Business Card for Mortuary

We need a business card design for our mortuary. We are not the "traditional" mortuary and specialize in simple cremations and burials. We use a two sided card.

Industry/Entity Type

Funeral Home

Contact Information for Business Card

One side we would like to have with the general information of the mortuary:
Address: 4127 E. Larkspur Ave, Sun City, AZ 85399
Phone: 623-555-0142
email: hello@willowbendmortuary.example
website: willowbendmortuary.example

On the other side would like to have the information of employee:
Name: Mark T. Ellis
Email: mark@willowbendmortuary.example
Title: Funeral Director
Text: 602-555-0187

Font styles to use
Serif
Sans Serif

Requirements
Should not have
• Do not put any gothic images or things like a hearse or tombstone.

```html
<!DOCTYPE html>
<html lang="en">
<head>
<meta charset="utf-8">
<title>Willowbend Mortuary – Business Card</title>
<link rel="stylesheet" href="https://fonts.googleapis.com/css2?family=Roboto:wght@400;500;700&family=Roboto+Condensed:wght@400;700&display=swap">
<style>
  :root {
    --page: #ffffff;
    --card-white: #ffffff;
    --charcoal: #4a4a4a;
    --stripe: #1c1c1c;
    --accent-green: #8bc34a;
    --tab-green: #86c24d;
    --tab-shadow: #2e2e2e;
    --ink: #111111;
    --light: #ffffff;
  }
  * { box-sizing: border-box; margin: 0; padding: 0; }
  html, body {
    width: 1200px; height: 1200px; overflow: hidden;
    background: var(--page);
  }
  .canvas { position: relative; width: 1200px; height: 1200px; }

  .card {
    position: absolute;
    width: 584px; height: 376px;
    border-radius: 0 27px 0 27px;
    overflow: hidden;
    box-shadow: 0 10px 22px rgba(0,0,0,0.28);
  }
  .card-front { left: 301px; top: 203px; background: var(--card-white); }
  .card-back  { left: 312px; top: 623px; background: var(--charcoal); }

  .card-shapes { position: absolute; inset: 0; }

  /* Front: brand name */
  .brand-dot {
    position: absolute; left: 270px; top: 84px;
    width: 26px; height: 26px; border-radius: 50%;
    background: var(--accent-green);
  }
  .brand-name {
    position: absolute; left: 306px; top: 80px;
    font-family: "Roboto", Arial, sans-serif;
    font-weight: 500; color: var(--light);
    font-size: 24px; line-height: 34px;
    white-space: nowrap;
  }
  .front-address {
    position: absolute; right: 33px; top: 154px;
    font-family: "Roboto Condensed", Arial, sans-serif;
    font-weight: 700; font-size: 13px; color: var(--light);
  }

  .contact-line {
    position: absolute; right: 83px;
    font-family: "Roboto Condensed", Arial, sans-serif;
    color: var(--ink); white-space: nowrap;
  }
  .contact-phone { top: 250px; font-size: 19px; }
  .contact-email { top: 291px; font-size: 15px; }
  .contact-web   { top: 325px; font-size: 15px; }

  /* Back: employee */
  .employee-name {
    position: absolute; right: 85px; top: 62px;
    font-family: "Roboto Condensed", Arial, sans-serif;
    font-weight: 700; font-size: 44px; color: var(--light);
  }
  .employee-title {
    position: absolute; right: 85px; top: 114px;
    font-family: "Roboto Condensed", Arial, sans-serif;
    font-size: 19px; color: var(--light);
  }
  .employee-email {
    position: absolute; right: 114px; top: 278px;
    font-family: "Roboto", Arial, sans-serif;
    font-size: 12.5px; color: var(--light);
  }
  .employee-email-icon { position: absolute; right: 84px; top: 280px; }
  .employee-text {
    position: absolute; right: 85px; top: 300px;
    font-family: "Roboto Condensed", Arial, sans-serif;
    font-size: 26px; color: var(--light);
  }
</style>
</head>
<body>
<main class="canvas">

  <section class="card card-front" aria-label="Business card front">
    <svg class="card-shapes" width="584" height="376" viewBox="0 0 584 376" aria-hidden="true">
      <polygon points="212,0 584,0 584,376 341,376" fill="var(--charcoal)"/>
      <polygon points="185,0 212,0 341,376 315,376" fill="var(--stripe)"/>

      <g class="tab-phone">
        <polygon points="256,255 540,255 540,279 264,279" fill="var(--tab-shadow)" opacity="0.6"/>
        <polygon points="252,249 532,249 532,273 260,273" fill="var(--tab-green)"/>
        <rect x="518" y="249" width="45" height="25" rx="12.5" fill="var(--stripe)"/>
        <path d="M543 255 c-2 0 -3 1 -3 2 c0 5 4 9 9 10 c1 0 2 -1 2 -3 l-2 -1 l-2 1 c-2 -1 -4 -3 -5 -5 l1 -2 z" fill="var(--light)"/>
      </g>
      <g class="tab-email">
        <polygon points="268,294 540,294 540,317 275,317" fill="var(--tab-shadow)" opacity="0.6"/>
        <polygon points="264,288 532,288 532,311 271,311" fill="var(--tab-green)"/>
        <rect x="518" y="288" width="45" height="24" rx="12" fill="var(--stripe)"/>
        <rect x="534" y="294" width="17" height="12" fill="none" stroke="var(--light)" stroke-width="1.6"/>
        <polyline points="534,294 542.5,301 551,294" fill="none" stroke="var(--light)" stroke-width="1.6"/>
      </g>
      <g class="tab-web">
        <polygon points="279,329 540,329 540,351 286,351" fill="var(--tab-shadow)" opacity="0.6"/>
        <polygon points="275,323 532,323 532,345 282,345" fill="var(--tab-green)"/>
        <rect x="518" y="322" width="45" height="24" rx="12" fill="var(--stripe)"/>
        <circle cx="542" cy="334" r="7.5" fill="none" stroke="var(--light)" stroke-width="1.5"/>
        <ellipse cx="542" cy="334" rx="3.2" ry="7.5" fill="none" stroke="var(--light)" stroke-width="1.2"/>
        <line x1="534.5" y1="334" x2="549.5" y2="334" stroke="var(--light)" stroke-width="1.2"/>
      </g>
    </svg>

    <div class="brand-dot" aria-hidden="true"></div>
    <div class="brand-name">Willowbend Mortuary</div>
    <p class="front-address">4127 E. Larkspur Ave, Sun City, AZ 85399</p>

    <p class="contact-line contact-phone">623-555-0142</p>
    <p class="contact-line contact-email">hello@willowbendmortuary.example</p>
    <p class="contact-line contact-web">willowbendmortuary.example</p>
  </section>

  <section class="card card-back" aria-label="Business card back">
    <h1 class="employee-name">Mark T. Ellis</h1>
    <p class="employee-title">Funeral Director</p>
    <p class="employee-email">mark@willowbendmortuary.example</p>
    <svg class="employee-email-icon" width="18" height="13" viewBox="0 0 18 13" aria-hidden="true">
      <rect x="1" y="1" width="16" height="11" fill="none" stroke="var(--light)" stroke-width="1.4"/>
      <polyline points="1,1 9,7 17,1" fill="none" stroke="var(--light)" stroke-width="1.4"/>
    </svg>
    <p class="employee-text">Text: 602-555-0187</p>
  </section>

</main>
</body>
</html>
```